KVO-Business Card Design

I need a modern, professional business card design that includes my logo as the main feature, maybe the entire background with the contact info overlaying or even contact info on the back and the logo full frontal

Neat and organized placement of contact information

Would like to see options in black and white

Target Market(s)

real estate Developers, Construction managers, business and home owners

Industry/Entity Type

Construction

Contact Information for Business Card

KVO Construction
Danny Ferrante
General Contractor

Office: 1-888-902-7315 Ext #1
Cell: 215-730-4162
Fax: 1-888-902-7315

Font styles to use
Serif

Requirements
Must have
• title
• office #
• cell #
• Email
• website
Nice to have
• fax

```html
<!DOCTYPE html>
<html lang="en">
<head>
<meta charset="utf-8">
<title>KVO Construction – Business Card</title>
<link href="https://fonts.googleapis.com/css2?family=Montserrat:wght@400;600;700&display=swap" rel="stylesheet">
<style>
  :root {
    --backdrop: #e9e6e1;
    --card-black: #0b0b0b;
    --card-sheen: #2a2a2a;
    --brand-green: #7ed348;
    --text-white: #f2f2f2;
    --rule-white: #d8d8d8;
  }
  * { box-sizing: border-box; margin: 0; padding: 0; }
  html, body {
    width: 1200px; height: 913px; overflow: hidden;
    background: var(--backdrop);
    font-family: "Montserrat", sans-serif;
  }
  .canvas { position: relative; width: 1200px; height: 913px; }
  .card {
    position: absolute;
    width: 525px; height: 300px;
    border-radius: 4px;
    background: linear-gradient(125deg, var(--card-black) 0%, var(--card-sheen) 45%, var(--card-black) 75%);
    box-shadow: 0 14px 30px rgba(0,0,0,.35);
    overflow: hidden;
    color: var(--text-white);
  }
  .card--front { left: 50px; top: 170px; }
  .card--back { left: 625px; top: 440px; }

  /* Front side */
  .brand-mark {
    position: absolute; left: 30px; top: 124px;
    display: flex; align-items: center; gap: 8px;
    font-weight: 700; font-size: 18px; letter-spacing: .5px;
    color: var(--brand-green); white-space: nowrap;
  }
  .brand-mark__dot { width: 11px; height: 11px; background: var(--brand-green); }
  .rule { position: absolute; height: 1px; background: var(--rule-white); }
  .rule--left { left: 0; top: 160px; width: 250px; }
  .rule--right { left: 448px; top: 92px; width: 77px; }
  .identity { position: absolute; left: 262px; top: 78px; }
  .identity__name { font-weight: 600; font-size: 22px; color: var(--brand-green); white-space: nowrap; }
  .identity__title { font-size: 13px; margin-top: 2px; }
  .contact-list {
    position: absolute; left: 278px; top: 140px;
    list-style: none; font-size: 12.5px; line-height: 19px;
  }
  .contact-list li { display: flex; align-items: center; gap: 9px; white-space: nowrap; }
  .contact-list svg { width: 10px; height: 10px; fill: var(--brand-green); flex: none; }

  /* Back side */
  .card--back .brand-mark {
    left: 0; right: 0; top: 96px; justify-content: center;
    font-size: 40px; gap: 14px; letter-spacing: 1px;
  }
  .card--back .brand-mark__dot { width: 18px; height: 18px; }
  .web-address {
    position: absolute; left: 0; right: 0; top: 190px;
    text-align: center; font-size: 16px; letter-spacing: .5px;
  }
  .web-address__domain { color: var(--brand-green); }
</style>
</head>
<body>
<main class="canvas">

  <section class="card card--front" aria-label="Business card front">
    <div class="brand-mark"><span class="brand-mark__dot"></span>KVO Construction</div>
    <div class="rule rule--left"></div>
    <div class="rule rule--right"></div>
    <div class="identity">
      <p class="identity__name">Danny Ferrante</p>
      <p class="identity__title">General Contractor</p>
    </div>
    <ul class="contact-list">
      <li><svg viewBox="0 0 10 10"><rect x="2" y="0" width="6" height="10" rx="1"/></svg>215-730-4162</li>
      <li><svg viewBox="0 0 10 10"><rect x="0" y="3" width="10" height="7" rx="1"/><rect x="2" y="0" width="6" height="3"/></svg>1-888-902-7315</li>
      <li><svg viewBox="0 0 10 10"><path d="M2 0l2 2-1 2c1 2 2 3 3 3l2-1 2 2-2 2C4 10 0 6 0 2z"/></svg>1-888-902-7315 Ext #1</li>
      <li><svg viewBox="0 0 10 10"><path d="M0 2h10v6H0zM0 2l5 4 5-4"/></svg>info@dannyferrante.com</li>
      <li><svg viewBox="0 0 10 10"><circle cx="5" cy="5" r="5"/></svg>www.kvoconstruction.com</li>
    </ul>
  </section>

  <section class="card card--back" aria-label="Business card back">
    <div class="brand-mark"><span class="brand-mark__dot"></span>KVO Construction</div>
    <p class="web-address">www.<span class="web-address__domain">kvoconstruction</span>.com</p>
  </section>

</main>
</body>
</html>
```